Plakat-Design für Immobilienunternehmen
Zielgruppe
Immobilienunternehmen
Aufgabenstellung
Das Plakat steht an der Strasse und muss beim Vorbeifahren gut erkennbar sein...
Es geht bei dem Plakat darum, dass wir die Bevölkerung einladen ein Immobilienprojekt vorzustellen...
Der Text kann jedoch gerne verändert werden, wichtig ist das die Botschaften rüberkommt
Länge: 340cm
Höhe: 173cm
TEXT:
Wir Informieren…
…über unseren Kupfa
Die Lobner Immobiliengruppe lädt zur
Informationsveranstaltung ein:
Wann: FR, 26.02.21 von 16:00 - 19:00 Uhr
SA, 27.02.21 von 10:00 - 13:00 Uhr
Wo: Vereinshaus Talbach
Wir präsentieren den Architekturwettbewerb Kupferhof den Bürgerinnen und Bürger.
(Gemeinde Talbach Logo). (HausKontor Logo).

```html
<!DOCTYPE html>
<html lang="de">
<head>
<meta charset="utf-8">
<title>Informationsveranstaltung Kupferhof</title>
<link rel="stylesheet" href="https://fonts.googleapis.com/css2?family=Montserrat:wght@400;500;800&display=swap">
<style>
  :root {
    --page-bg: #e4e4e2;
    --banner-bg: #ffffff;
    --ink: #1d1d1d;
    --green: #27a050;
    --green-dark: #1f8f46;
    --photo-model: #e7e7e7;
    --photo-render-top: #cfcfcc;
    --photo-render-bottom: #8d8a83;
    --town-blue: #1d3f8a;
  }
  * { box-sizing: border-box; margin: 0; padding: 0; }
  html, body {
    width: 1200px; height: 843px; overflow: hidden;
    background: var(--page-bg);
    font-family: "Montserrat", Arial, sans-serif;
    color: var(--ink);
  }
  .banner {
    position: absolute; left: 30px; top: 131px;
    width: 1140px; height: 580px;
    background: var(--banner-bg);
    box-shadow: 0 6px 18px rgba(0,0,0,.18);
    overflow: hidden;
  }
  .banner-frame {
    position: absolute; left: 38px; top: 30px; right: 38px; bottom: 36px;
    border: 2px solid var(--ink);
  }
  .headline {
    position: absolute; left: 0; right: 0; top: 44px;
    text-align: center; font-weight: 800;
    font-size: 49px; line-height: 56px; letter-spacing: 1px;
    text-transform: uppercase;
  }
  .subline {
    position: absolute; left: 0; right: 0; top: 158px;
    text-align: center; font-size: 16px; font-weight: 400;
  }
  .invite-band {
    position: absolute; left: 0; right: 0; top: 190px; height: 136px;
    background: var(--green); color: #fff;
  }
  .invite-band .lead {
    position: absolute; left: 0; right: 0; top: 18px;
    text-align: center; font-size: 14.5px; letter-spacing: 1.4px;
  }
  .event-dates {
    position: absolute; left: 218px; top: 62px;
    display: flex; align-items: center; gap: 22px;
  }
  .event-dates p, .event-place p {
    font-size: 17px; letter-spacing: 1.2px; line-height: 26px;
  }
  .event-place {
    position: absolute; left: 710px; top: 60px;
    display: flex; align-items: center; gap: 22px;
  }
  .model-photo {
    position: absolute; left: 60px; top: 352px; width: 272px; height: 200px;
    background: linear-gradient(135deg, #f1f1f1, var(--photo-model) 60%, #dadada);
  }
  .facts {
    position: absolute; left: 355px; top: 346px; width: 300px;
    font-size: 13.5px; line-height: 23px;
  }
  .facts dl { display: grid; grid-template-columns: 1fr 70px; }
  .facts dd { padding-left: 6px; }
  .facts .note { margin-top: 14px; line-height: 20px; }
  .render-photo {
    position: absolute; left: 690px; top: 342px; width: 318px; height: 192px;
    background: linear-gradient(180deg, var(--photo-render-top), #b3b0a9 55%, var(--photo-render-bottom));
  }
  .partner-names {
    position: absolute; right: 48px; top: 470px;
    display: flex; flex-direction: column; align-items: flex-end; gap: 16px;
  }
  .partner-name { font-weight: 800; font-size: 13px; color: var(--green-dark); }
  .partner-name.town { color: var(--town-blue); font-size: 9px; letter-spacing: 1.6px; display: flex; align-items: center; gap: 5px; }
  .partner-name.town .mark { width: 10px; height: 10px; background: var(--town-blue); }
</style>
</head>
<body>
  <section class="banner">
    <div class="banner-frame"></div>

    <h1 class="headline">Wir informieren Sie<br>über unseren Kupfa</h1>
    <p class="subline">Wir präsentieren den Architekturwettbewerb Kupferhof den Bürgerinnen und Bürger.</p>

    <div class="invite-band">
      <p class="lead">Die Lobner Immobiliengruppe lädt zur Informationsveranstaltung ein:</p>
      <div class="event-dates">
        <svg width="40" height="44" viewBox="0 0 40 44" aria-hidden="true">
          <rect x="2" y="5" width="36" height="37" rx="3" fill="none" stroke="#fff" stroke-width="2"/>
          <line x1="2" y1="13" x2="38" y2="13" stroke="#fff" stroke-width="2"/>
          <line x1="10" y1="1" x2="10" y2="9" stroke="#fff" stroke-width="2"/>
          <line x1="30" y1="1" x2="30" y2="9" stroke="#fff" stroke-width="2"/>
          <text x="20" y="36" text-anchor="middle" fill="#fff" font-family="Montserrat, sans-serif" font-size="17">31</text>
        </svg>
        <div>
          <p>FR, 26.02.21 von 16:00 - 19:00 Uhr</p>
          <p>SA, 27.02.21 von 10:00 - 13:00 Uhr</p>
        </div>
      </div>
      <div class="event-place">
        <svg width="30" height="42" viewBox="0 0 30 42" aria-hidden="true">
          <path d="M15 40 C5 27 2 21 2 14 A13 13 0 0 1 28 14 C28 21 25 27 15 40 Z" fill="none" stroke="#fff" stroke-width="2"/>
          <circle cx="15" cy="14" r="5.5" fill="none" stroke="#fff" stroke-width="2"/>
        </svg>
        <p>Vereinshaus Talbach</p>
      </div>
    </div>

    <div class="model-photo" role="img" aria-label="Foto des weißen Architekturmodells mit Lageplan"></div>

    <div class="facts">
      <dl>
        <dt>Wohnungsanzahl:</dt><dd>44 Stk.</dd>
        <dt>Wohnnutzflächen Netto:</dt><dd>1.970 m²</dd>
        <dt>Stellplätze gesamt:</dt><dd>88 Stk.</dd>
        <dt>Stellplätze Wohnungen:</dt><dd>51 Stk.</dd>
        <dt>Stellplätze Gewerbe:</dt><dd>37 Stk.</dd>
      </dl>
      <p class="note">Skybar, die durch den 360°-Rundumblick<br>“Kupferhof“ im Erdgeschoß an<br>der Ecke Lindenstraße-Mühlweg</p>
    </div>

    <div class="render-photo" role="img" aria-label="Visualisierung des geplanten Wohngebäudes mit Vorplatz"></div>

    <div class="partner-names">
      <span class="partner-name">HausKontor</span>
      <span class="partner-name town"><span class="mark"></span>MARKTGEMEINDE TALBACH</span>
    </div>
  </section>
</body>
</html>
```